Innovative healthcare collaborative needs new look for business cards

CareLoomQ is a new kind of healthcare relationship company focused on aligning partners, innovation and solutions to provide needed health services to healthcare systems, hospitals or private business. Not mired in the old merger and acquisition fee-for-service framework, we focus on primary, secondary and tertiary service area partnership collaboratives. These networks are constructed by aligning healthcare services along a network of care, not just an individual patient care plan. This involves partnership arrangements with large or small medical centers, physician groups, allied health services, public health agencies, health insurers, et al as well as civic agencies, schools, farmers, supply chains to bring about needed healthcare solutions for patients. Think Amber Fields. AF does for communities what we do for hospitals and health systems. We educate and instruct on strategic, operational, and innovative solutions for a healthcare provider, practice, business, or system resulting in successful construction of care networks (legal entity). We provide the blueprint of how to do this type of partnership, focused on what’s best for the sustainability of the business and the people (patients or potential patients) living there. Rural hospitals in particular are at risk.
We also provide seminars to academic, medical academic, and private industry to instruct on how to construct these care networks and educate on the essential criteria to be successful in the new healthcare era. We have been doing this work for the past 8 years, and since COVID-19, the recognition of fractured processes has boosted the demand. We need a business card that sets the tone that the traditional healthcare delivery system in the US has transformed (overnight). Our company is educating on how to transition current business models to the new world order in this space.
Brainstormed some business card tag lines for consideration:
CareLoomQ
• a healthcaring company
• allbettertogether
• connecting for the greater good

Target Market(s)

Health systems, hospitals, physician practices, academic medical schools, residency programs

Industry/Entity Type

Healthcare

Contact Information for Business Card

Doreen Vasquell, Chief Relationship Officer
doreenvasquell@mailbrook.example
mobile: 412-806-2394

Font styles to use
Serif
Sans Serif

Requirements
Should not have
• Do not use word Consultant

```html
<!DOCTYPE html>
<html lang="en">
<head>
<meta charset="utf-8">
<title>CareLoomQ Business Card</title>
<link rel="stylesheet" href="https://fonts.googleapis.com/css2?family=Lato:wght@400;700;900&display=swap">
<style>
  :root {
    --backdrop: #d6d6d6;
    --card-light: #ffffff;
    --card-dark: #000000;
    --ink: #0a0a0a;
    --ink-soft: #4a4a4a;
    --paper: #ffffff;
  }
  * { margin: 0; padding: 0; box-sizing: border-box; }
  html, body {
    width: 1200px;
    height: 1143px;
    overflow: hidden;
    background: var(--backdrop);
    font-family: "Lato", sans-serif;
  }
  .card {
    position: absolute;
    left: 299px;
    width: 602px;
    height: 344px;
  }
  .card-front { top: 180px; background: var(--card-light); }
  .card-back { top: 621px; background: var(--card-dark); }

  .brand-name {
    position: absolute;
    font-family: "Lato", sans-serif;
    font-weight: 900;
    letter-spacing: 0.5px;
    line-height: 1;
    white-space: nowrap;
  }
  .card-front .brand-name {
    right: 36px;
    top: 70px;
    font-size: 46px;
    color: var(--ink);
  }
  .card-back .brand-name {
    left: 0;
    right: 0;
    text-align: center;
    top: 178px;
    font-size: 56px;
    color: var(--paper);
  }

  .accent-bar {
    position: absolute;
    left: 0;
    top: 208px;
    width: 10px;
    height: 41px;
    background: var(--ink);
  }
  .holder {
    position: absolute;
    left: 38px;
    top: 204px;
  }
  .holder-name {
    font-weight: 700;
    font-size: 29px;
    line-height: 34px;
    color: var(--ink);
  }
  .holder-title {
    font-weight: 400;
    font-size: 16px;
    line-height: 20px;
    color: var(--ink-soft);
  }
  .contact-list {
    position: absolute;
    left: 38px;
    top: 273px;
    list-style: none;
  }
  .contact-item {
    display: flex;
    align-items: center;
    height: 22px;
    font-size: 16px;
    color: var(--ink-soft);
  }
  .contact-icon {
    width: 16px;
    height: 16px;
    margin-right: 13px;
    flex: none;
  }
</style>
</head>
<body>
  <section class="card card-front">
    <div class="brand-name">CareLoomQ</div>
    <div class="accent-bar"></div>
    <div class="holder">
      <div class="holder-name">Doreen Vasquell</div>
      <div class="holder-title">Chief Relationship Officer</div>
    </div>
    <ul class="contact-list">
      <li class="contact-item">
        <svg class="contact-icon" viewBox="0 0 24 24" aria-hidden="true">
          <path fill="#0a0a0a" d="M6.6 10.8a15.1 15.1 0 0 0 6.6 6.6l2.2-2.2a1 1 0 0 1 1-.25 11.4 11.4 0 0 0 3.6.57 1 1 0 0 1 1 1V20a1 1 0 0 1-1 1A17 17 0 0 1 3 4a1 1 0 0 1 1-1h3.5a1 1 0 0 1 1 1c0 1.25.2 2.45.57 3.6a1 1 0 0 1-.25 1z"/>
          <path fill="none" stroke="#0a0a0a" stroke-width="2" d="M14 2.5a8 8 0 0 1 7.5 7.5M14 6.5a4 4 0 0 1 3.5 3.5"/>
        </svg>
        412-806-2394
      </li>
      <li class="contact-item">
        <svg class="contact-icon" viewBox="0 0 24 24" aria-hidden="true">
          <rect x="1" y="4" width="22" height="16" fill="#0a0a0a"/>
          <path fill="none" stroke="#ffffff" stroke-width="1.6" d="M2 5l10 8 10-8M2 19l7.5-7M22 19l-7.5-7"/>
        </svg>
        doreenvasquell@mailbrook.example
      </li>
    </ul>
  </section>

  <section class="card card-back">
    <div class="brand-name">CareLoomQ</div>
  </section>
</body>
</html>
```